Harbourne Computer Repairs Web Banner

We're after a catchy web banner to advertise the computer repairs business on other web sites and affiliate sites. We manage software, hardware repairs, component upgrades, virus and malware removal and provide online backup solutions.
Please incorporate the logo designed by Pixo, and add our phone number, 1300 482 956 to the banner. The banner will link to the website homepage.

```html
<!DOCTYPE html>
<html lang="en">
<head>
<meta charset="utf-8">
<title>Harbourne Computer Repairs – Web Banner Set</title>
<link href="https://fonts.googleapis.com/css2?family=Exo:wght@500;600&family=Arimo:wght@700&display=swap" rel="stylesheet">
<style>
  :root{
    --stage:#e9e6e1;
    --panel:#1f2022;
    --panel-hi:#2a2b2e;
    --phone-bar:#161718;
    --light:#e8e8e8;
    --light-lo:#c9c9c9;
    --edge:#2f6fd6;
    --grey-text:#b9b9b9;
    --soft-blue:#d8f0ff;
    --glow-blue:#3aa8ff;
    --soft-red:#ffd0d0;
    --glow-red:#ff3b3b;
    --soft-green:#e4ffd8;
    --glow-green:#5ad13a;
    --btn-top:#ffe34a;
    --btn-bot:#f5a300;
    --btn-text:#5a3a00;
    --brand:#4aa6f0;
  }
  *{box-sizing:border-box;margin:0;padding:0}
  html,body{width:1200px;height:891px;overflow:hidden;background:var(--stage)}
  .stage{position:relative;width:1200px;height:891px}

  .banner{position:absolute;background:linear-gradient(180deg,var(--panel-hi),var(--panel));
    font-family:"Exo",sans-serif;color:#fff;overflow:hidden;
    box-shadow:0 3px 8px rgba(0,0,0,.35)}
  .brand{font-family:"Exo",sans-serif;font-weight:600;color:var(--brand);text-align:center;line-height:1.1}
  .services{list-style:none;font-weight:500}
  .services li{white-space:nowrap}
  .s-blue{color:var(--soft-blue);text-shadow:0 0 4px var(--glow-blue)}
  .s-red{color:var(--soft-red);text-shadow:0 0 4px var(--glow-red)}
  .s-green{color:var(--soft-green);text-shadow:0 0 4px var(--glow-green)}
  .phone-number{font-family:"Arimo",sans-serif;font-weight:700;color:var(--grey-text);white-space:nowrap}
  .phone-icon{fill:#9a9a9a}
  .light-zone{background:linear-gradient(180deg,var(--light),var(--light-lo));display:flex;align-items:center}
  .repair-icon{background:radial-gradient(ellipse at 50% 50%,#4b8fe0 0,#1c55b0 55%,transparent 72%);border-radius:50%}
  .cta{font-family:"Arimo",sans-serif;font-weight:700;color:var(--btn-text);
    background:linear-gradient(180deg,var(--btn-top),var(--btn-bot));border-radius:999px;
    display:flex;align-items:center;justify-content:center;white-space:nowrap;
    box-shadow:0 1px 2px rgba(0,0,0,.4),inset 0 1px 0 rgba(255,255,255,.6)}

  /* Leaderboard 728x90 */
  .leaderboard{left:101px;top:40px;width:756px;height:94px;border-left:3px solid var(--edge);border-right:6px solid var(--edge);display:flex}
  .leaderboard .brand{width:175px;font-size:17px;align-self:center;padding-left:10px}
  .leaderboard .services{width:255px;text-align:right;font-size:14.5px;line-height:17.5px;padding-top:2px}
  .leaderboard .phone-block{width:160px;display:flex;flex-direction:column;align-items:center;justify-content:center;gap:4px}
  .leaderboard .phone-number{font-size:22px}
  .leaderboard .light-zone{flex:1;flex-direction:column;justify-content:center;gap:6px}
  .leaderboard .repair-icon{width:62px;height:36px}
  .leaderboard .cta{width:114px;height:26px;font-size:14px}

  /* Banner 468x60 */
  .fullbanner{left:101px;top:148px;width:486px;height:63px;border-left:2px solid var(--edge);border-right:4px solid var(--edge);display:flex}
  .fullbanner .brand{width:120px;font-size:11px;align-self:center;padding-left:6px}
  .fullbanner .services{width:160px;text-align:right;font-size:9px;line-height:11.4px;padding-top:2px}
  .fullbanner .phone-block{width:110px;display:flex;flex-direction:column;align-items:center;justify-content:center;gap:2px}
  .fullbanner .phone-number{font-size:14px}
  .fullbanner .light-zone{flex:1;flex-direction:column;justify-content:center;gap:4px}
  .fullbanner .repair-icon{width:44px;height:24px}
  .fullbanner .cta{width:74px;height:17px;font-size:9px}

  /* Skyscrapers */
  .tower{top:227px;height:623px;border-top:4px solid var(--edge);display:flex;flex-direction:column}
  .tower .brand{height:80px;display:flex;align-items:center;justify-content:center;padding:0 6px}
  .tower .services{flex:1;text-align:center;display:flex;flex-direction:column;gap:14px;padding-top:12px}
  .tower .services li{white-space:normal}
  .tower .phone-block{height:90px;background:var(--phone-bar);display:flex;flex-direction:column;align-items:center;justify-content:center;gap:8px}
  .tower .light-zone{height:126px;flex-direction:column;justify-content:center;gap:14px;border-bottom:5px solid var(--edge)}
  .sky-wide{left:101px;width:166px}
  .sky-wide .brand{font-size:17px}
  .sky-wide .services{font-size:20px;line-height:22px}
  .sky-wide .phone-number{font-size:22px}
  .sky-wide .repair-icon{width:76px;height:46px}
  .sky-wide .cta{width:146px;height:36px;font-size:18px}
  .sky-narrow{left:283px;width:125px}
  .sky-narrow .brand{font-size:13px}
  .sky-narrow .services{font-size:17px;line-height:20px}
  .sky-narrow .phone-number{font-size:17px}
  .sky-narrow .repair-icon{width:66px;height:42px}
  .sky-narrow .cta{width:110px;height:30px;font-size:14px}

  /* Box formats */
  .box{display:flex;flex-direction:column;border-top:4px solid var(--edge)}
  .box .brand{display:flex;align-items:center;justify-content:center;position:relative}
  .box .brand::before,.box .brand::after{content:"";position:absolute;top:30%;width:16%;height:40%;
    background:linear-gradient(180deg,transparent 0 18%,var(--glow-blue) 18% 22%,transparent 22% 48%,var(--glow-red) 48% 52%,transparent 52% 78%,var(--glow-green) 78% 82%,transparent 82%);opacity:.8}
  .box .brand::before{left:4%}
  .box .brand::after{right:4%}
  .box .services{text-align:center;flex:1}
  .box .services li{display:flex;align-items:center;justify-content:center;gap:6px}
  .box .services li::before,.box .services li::after{content:"";height:1px;width:40px;background:currentColor;opacity:.6}
  .box .phone-block{background:var(--phone-bar);display:flex;align-items:center;justify-content:center;gap:6px}
  .box .light-zone{justify-content:space-around;border-bottom:4px solid var(--edge)}

  .rect-large{left:424px;top:227px;width:349px;height:291px}
  .rect-large .brand{height:78px;font-size:16px}
  .rect-large .services{font-size:16px;line-height:19.5px}
  .rect-large .phone-block{height:30px}
  .rect-large .phone-number{font-size:22px}
  .rect-large .light-zone{height:66px}
  .rect-large .repair-icon{width:100px;height:50px}
  .rect-large .cta{width:148px;height:36px;font-size:18px}

  .rect-medium{left:788px;top:227px;width:311px;height:260px}
  .rect-medium .brand{height:67px;font-size:15px}
  .rect-medium .services{font-size:14px;line-height:17.5px}
  .rect-medium .phone-block{height:28px}
  .rect-medium .phone-number{font-size:20px}
  .rect-medium .light-zone{height:56px}
  .rect-medium .repair-icon{width:84px;height:42px}
  .rect-medium .cta{width:132px;height:32px;font-size:16px}

  .square{left:424px;top:534px;width:260px;height:260px}
  .square .brand{height:67px;font-size:13px}
  .square .services{font-size:14px;line-height:17.5px}
  .square .phone-block{height:28px}
  .square .phone-number{font-size:20px}
  .square .light-zone{height:61px}
  .square .repair-icon{width:64px;height:42px}
  .square .cta{width:130px;height:34px;font-size:16px}

  .square-small{left:700px;top:534px;width:208px;height:208px}
  .square-small .brand{height:50px;font-size:11px}
  .square-small .services{font-size:11px;line-height:14px}
  .square-small .services li::before,.square-small .services li::after{width:18px}
  .square-small .phone-block{height:22px}
  .square-small .phone-number{font-size:16px}
  .square-small .light-zone{height:50px}
  .square-small .repair-icon{width:50px;height:32px}
  .square-small .cta{width:104px;height:26px;font-size:13px}
</style>
</head>
<body>
<svg width="0" height="0" style="position:absolute" aria-hidden="true">
  <symbol id="phone" viewBox="0 0 40 32">
    <path d="M3 9c0-4 7-7 17-7s17 3 17 7v3h-8v-3c-3-1-6-1-9-1s-6 0-9 1v3H3z"/>
    <path d="M10 12h20l6 16c0 2-1 3-3 3H7c-2 0-3-1-3-3z"/>
    <g fill="#1f2022"><rect x="13" y="16" width="3" height="2"/><rect x="19" y="16" width="3" height="2"/><rect x="25" y="16" width="3" height="2"/><rect x="13" y="20" width="3" height="2"/><rect x="19" y="20" width="3" height="2"/><rect x="25" y="20" width="3" height="2"/><rect x="13" y="24" width="3" height="2"/><rect x="19" y="24" width="3" height="2"/><rect x="25" y="24" width="3" height="2"/></g>
  </symbol>
</svg>

<main class="stage">

  <a class="banner leaderboard" aria-label="Harbourne Computer Repairs 728 by 90 banner">
    <div class="brand">Harbourne Computer Repairs</div>
    <ul class="services">
      <li class="s-blue">Software Management</li>
      <li class="s-red">Hardware Repairs</li>
      <li class="s-green">Component Upgrades</li>
      <li class="s-red">Virus Removal</li>
      <li class="s-blue">Online Backup Solutions</li>
    </ul>
    <div class="phone-block">
      <svg class="phone-icon" width="54" height="42"><use href="#phone"/></svg>
      <span class="phone-number">1300 482 956</span>
    </div>
    <div class="light-zone">
      <div class="repair-icon" role="img" aria-label="Laptop with magnifier and tools repair icon"></div>
      <span class="cta">CLICK HERE</span>
    </div>
  </a>

  <a class="banner fullbanner" aria-label="Harbourne Computer Repairs 468 by 60 banner">
    <div class="brand">Harbourne Computer Repairs</div>
    <ul class="services">
      <li class="s-blue">Software Management</li>
      <li class="s-red">Hardware Repairs</li>
      <li class="s-green">Component Upgrades</li>
      <li class="s-red">Virus Removal</li>
      <li class="s-blue">Online Backup Solutions</li>
    </ul>
    <div class="phone-block">
      <svg class="phone-icon" width="34" height="26"><use href="#phone"/></svg>
      <span class="phone-number">1300 482 956</span>
    </div>
    <div class="light-zone">
      <div class="repair-icon" role="img" aria-label="Laptop with magnifier and tools repair icon"></div>
      <span class="cta">CLICK HERE</span>
    </div>
  </a>

  <a class="banner tower sky-wide" aria-label="Harbourne Computer Repairs 160 by 600 banner">
    <div class="brand">Harbourne Computer Repairs</div>
    <ul class="services">
      <li class="s-blue">Software Management</li>
      <li class="s-red">Hardware Repairs</li>
      <li class="s-green">Component Upgrades</li>
      <li class="s-red">Virus Removal</li>
      <li class="s-blue">Online Backup Solutions</li>
    </ul>
    <div class="phone-block">
      <svg class="phone-icon" width="60" height="48"><use href="#phone"/></svg>
      <span class="phone-number">1300 482 956</span>
    </div>
    <div class="light-zone">
      <div class="repair-icon" role="img" aria-label="Laptop with magnifier and tools repair icon"></div>
      <span class="cta">CLICK HERE</span>
    </div>
  </a>

  <a class="banner tower sky-narrow" aria-label="Harbourne Computer Repairs 120 by 600 banner">
    <div class="brand">Harbourne Computer Repairs</div>
    <ul class="services">
      <li class="s-blue">Software Management</li>
      <li class="s-red">Hardware Repairs</li>
      <li class="s-green">Component Upgrades</li>
      <li class="s-red">Virus Removal</li>
      <li class="s-blue">Online Backup Solutions</li>
    </ul>
    <div class="phone-block">
      <svg class="phone-icon" width="54" height="44"><use href="#phone"/></svg>
      <span class="phone-number">1300 482 956</span>
    </div>
    <div class="light-zone">
      <div class="repair-icon" role="img" aria-label="Laptop with magnifier and tools repair icon"></div>
      <span class="cta">CLICK HERE</span>
    </div>
  </a>

  <a class="banner box rect-large" aria-label="Harbourne Computer Repairs 336 by 280 banner">
    <div class="brand">Harbourne Computer<br>Repairs</div>
    <ul class="services">
      <li class="s-blue">Software Management</li>
      <li class="s-red">Hardware Repairs</li>
      <li class="s-green">Component Upgrades</li>
      <li class="s-red">Virus Removal</li>
      <li class="s-blue">Online Backup Solutions</li>
    </ul>
    <div class="phone-block">
      <svg class="phone-icon" width="24" height="19"><use href="#phone"/></svg>
      <span class="phone-number">1300 482 956</span>
    </div>
    <div class="light-zone">
      <div class="repair-icon" role="img" aria-label="Laptop with magnifier and tools repair icon"></div>
      <span class="cta">CLICK HERE</span>
    </div>
  </a>

  <a class="banner box rect-medium" aria-label="Harbourne Computer Repairs 300 by 250 banner">
    <div class="brand">Harbourne Computer<br>Repairs</div>
    <ul class="services">
      <li class="s-blue">Software Management</li>
      <li class="s-red">Hardware Repairs</li>
      <li class="s-green">Component Upgrades</li>
      <li class="s-red">Virus Removal</li>
      <li class="s-blue">Online Backup Solutions</li>
    </ul>
    <div class="phone-block">
      <svg class="phone-icon" width="22" height="17"><use href="#phone"/></svg>
      <span class="phone-number">1300 482 956</span>
    </div>
    <div class="light-zone">
      <div class="repair-icon" role="img" aria-label="Laptop with magnifier and tools repair icon"></div>
      <span class="cta">CLICK HERE</span>
    </div>
  </a>

  <a class="banner box square" aria-label="Harbourne Computer Repairs 250 by 250 banner">
    <div class="brand">Harbourne Computer<br>Repairs</div>
    <ul class="services">
      <li class="s-blue">Software Management</li>
      <li class="s-red">Hardware Repairs</li>
      <li class="s-green">Component Upgrades</li>
      <li class="s-red">Virus Removal</li>
      <li class="s-blue">Online Backup Solutions</li>
    </ul>
    <div class="phone-block">
      <svg class="phone-icon" width="22" height="17"><use href="#phone"/></svg>
      <span class="phone-number">1300 482 956</span>
    </div>
    <div class="light-zone">
      <div class="repair-icon" role="img" aria-label="Laptop with magnifier and tools repair icon"></div>
      <span class="cta">CLICK HERE</span>
    </div>
  </a>

  <a class="banner box square-small" aria-label="Harbourne Computer Repairs 200 by 200 banner">
    <div class="brand">Harbourne Computer<br>Repairs</div>
    <ul class="services">
      <li class="s-blue">Software Management</li>
      <li class="s-red">Hardware Repairs</li>
      <li class="s-green">Component Upgrades</li>
      <li class="s-red">Virus Removal</li>
      <li class="s-blue">Online Backup Solutions</li>
    </ul>
    <div class="phone-block">
      <svg class="phone-icon" width="18" height="14"><use href="#phone"/></svg>
      <span class="phone-number">1300 482 956</span>
    </div>
    <div class="light-zone">
      <div class="repair-icon" role="img" aria-label="Laptop with magnifier and tools repair icon"></div>
      <span class="cta">CLICK HERE</span>
    </div>
  </a>

</main>
</body>
</html>
```